Accountancy firm needs clean and simple website and optional logo

We need a logo and basic wordpress website design for a Sydney based accountancy firm.
We need a clean and simple logo and website, based on the accounting/finance/tax industry. Simple, credible and official colors.
The logo is expected to be so simple that we have combined into the one job.
If you submit a logo design and we choose it along with someone else's website design you will be paid a bonus of $60. The website design will still win the competition as per normal.
Current website is old and terrible but gives you an idea of the sitemap (super simple) and what they do: www.brookfiscal.com.au
We want original different to normal template looking designs.
We like videos, and like http://www.whitfords.com.au/
Feel free to go to vidhaven and use some videos from there.
We are based in Sydney Australia and in the field of taxation and accounting
We want a clean, formal, credible site, limited pages.
The project is guaranteed, so go for it.
Brook & Associates
1 page

```html
<!DOCTYPE html>
<html lang="en">
<head>
<meta charset="utf-8">
<title>Brook & Associates – Tax Accountants</title>
<link href="https://fonts.googleapis.com/css2?family=Roboto:ital,wght@0,300;0,400;0,500;0,700;1,400&display=swap" rel="stylesheet">
<style>
:root{
  --blue:#0b88dc;
  --blue-btn:#0a7fd2;
  --blue-deep:#0868ad;
  --field:#2a98e2;
  --ink:#444;
  --muted:#8c8c8c;
  --light:#f5f5f5;
  --footer:#353535;
  --white:#fff;
}
*{margin:0;padding:0;box-sizing:border-box}
html,body{width:794px;height:1200px;overflow:hidden}
body{font-family:'Roboto',sans-serif;background:var(--light);color:var(--ink);position:relative}

.site-header{position:absolute;left:0;top:0;width:794px;height:73px;background:var(--white);border-top:2px solid var(--blue)}
.brand{position:absolute;left:57px;top:8px;display:flex;align-items:flex-end;gap:9px}
.brand-mark{width:53px;height:53px;background:var(--blue)}
.brand-name{font-size:9.5px;font-weight:700;color:#222;letter-spacing:.3px;line-height:1.15;padding-bottom:1px;white-space:nowrap}
.brand-name span{display:block;font-weight:400;font-size:8.5px;letter-spacing:0;color:#222}
.main-nav a{position:absolute;top:33px;font-size:8px;color:#444;text-decoration:none;letter-spacing:.3px;white-space:nowrap}
.search-btn{position:absolute;left:712px;top:24px;width:26px;height:26px;border-radius:50%;background:var(--blue)}

.hero{position:absolute;left:0;top:73px;width:794px;height:322px;background:linear-gradient(180deg,#2a3a4f 0%,#3d4f66 45%,#2d3f55 70%,#1d2b3d 100%)}
.hero-photo{position:absolute;inset:0}
.hero-title{position:absolute;left:57px;top:89px;font-size:21px;font-weight:700;color:var(--white);letter-spacing:.2px;white-space:nowrap}
.hero-text{position:absolute;left:57px;top:127px;font-size:8.3px;font-style:italic;color:var(--white);line-height:19px;white-space:nowrap}
.btn{position:absolute;background:var(--blue-btn);color:var(--white);font-weight:500;text-align:center;text-transform:uppercase;white-space:nowrap}
.hero .btn{left:57px;top:197px;width:90px;height:29px;line-height:29px;font-size:10.5px}
.slide-arrow{position:absolute;top:147px;width:28px;height:28px;border:1.5px solid var(--white);border-radius:50%}

.contact-bar{position:absolute;left:57px;top:367px;width:680px;height:72px;background:var(--blue)}
.contact-bar .frame{position:absolute;left:5px;top:5px;right:5px;bottom:5px;border:1px solid rgba(255,255,255,.35)}
.contact-item{position:absolute;top:5px;height:62px;display:flex;align-items:center;gap:10px;color:var(--white);white-space:nowrap}
.contact-item .label{font-size:8px;text-transform:uppercase;letter-spacing:.2px}
.contact-item .value{font-size:10px;font-weight:500;line-height:13px}
.contact-item .value.big{font-size:13.5px;font-weight:700}
.divider{position:absolute;top:5px;width:1px;height:62px;background:rgba(255,255,255,.35)}

.section-title{position:absolute;left:0;width:794px;text-align:center;font-size:18px;font-weight:500;color:#444}
.section-lead{position:absolute;left:0;width:794px;text-align:center;font-size:8.3px;color:#666;line-height:14.5px}

.service-card{position:absolute;top:547px;width:215px;height:301px;background:var(--white);border:1px solid #e8e8e8}
.service-card .photo{height:134px}
.service-card .num{position:absolute;left:13px;top:146px;font-size:24px;font-weight:300;color:#d3d3d3}
.service-card h3{position:absolute;left:53px;top:153px;font-size:14px;font-weight:400;color:#444;white-space:nowrap}
.service-card p{position:absolute;left:16px;top:188px;width:188px;font-size:8.2px;color:var(--muted);line-height:15.2px}
.service-card .btn{left:17px;top:259px;width:87px;height:25px;line-height:25px;font-size:8px}

.quote{position:absolute;left:0;top:877px;width:794px;height:269px}
.quote-photo{position:absolute;left:0;top:0;width:400px;height:269px;background:linear-gradient(180deg,#5c6f8a 0%,#8a6f4e 45%,#3a3e4c 75%,#1e2433 100%)}
.quote-panel{position:absolute;left:400px;top:0;width:394px;height:269px;background:var(--blue);color:var(--white)}
.quote-panel h2{position:absolute;left:0;top:20px;width:394px;text-align:center;font-size:18px;font-weight:700}
.quote-panel .lead{position:absolute;left:0;top:49px;width:394px;text-align:center;font-size:8.3px;line-height:14.5px;white-space:nowrap}
.field{position:absolute;background:var(--field);font-size:8.3px;padding:10px 0 0 10px;color:var(--white)}
.subscribe{position:absolute;left:124px;top:224px;width:102px;height:27px;background:var(--blue-deep);font-size:10px;font-weight:500;text-align:center;line-height:27px}

.site-footer{position:absolute;left:0;top:1146px;width:794px;height:54px;background:var(--footer)}
.copyright{position:absolute;left:57px;top:21px;font-size:8px;color:#ddd;white-space:nowrap}
.social{position:absolute;top:14px;width:26px;height:26px;border:1.5px solid var(--white);border-radius:50%}
</style>
</head>
<body>

<header class="site-header">
  <div class="brand">
    <div class="brand-mark"></div>
    <div class="brand-name">BROOK &amp; ASSOCIATES<span>tax accountants</span></div>
  </div>
  <nav class="main-nav">
    <a href="#" style="left:506px">HOME</a>
    <a href="#" style="left:571px">ABOUT US</a>
    <a href="#" style="left:652px">CONTACT US</a>
  </nav>
  <div class="search-btn">
    <svg width="26" height="26" viewBox="0 0 26 26"><circle cx="12" cy="12" r="3.2" fill="none" stroke="#fff" stroke-width="1.6"/><line x1="14.4" y1="14.4" x2="16.5" y2="16.5" stroke="#fff" stroke-width="1.8" stroke-linecap="round"/></svg>
  </div>
</header>

<section class="hero">
  <div class="hero-photo" role="img" aria-label="Harbour waterfront with a lit concert hall at dusk"></div>
  <h1 class="hero-title">WELCOME TO BROOK TAX</h1>
  <p class="hero-text">It is a long established fact that a reader will be distracted by the read-<br>able content of a page when looking at its layout. The point of using as<br>opposed tomaking it look like readable English.</p>
  <a class="btn">Read More</a>
  <div class="slide-arrow" style="left:16px"><svg width="25" height="25" viewBox="0 0 25 25"><polyline points="14,7.5 9,12.5 14,17.5" fill="none" stroke="#fff" stroke-width="2"/></svg></div>
  <div class="slide-arrow" style="left:742px"><svg width="25" height="25" viewBox="0 0 25 25"><polyline points="11,7.5 16,12.5 11,17.5" fill="none" stroke="#fff" stroke-width="2"/></svg></div>
</section>

<section class="contact-bar">
  <div class="frame"></div>
  <div class="contact-item" style="left:18px">
    <svg width="18" height="18" viewBox="0 0 24 24"><path d="M6.6 10.8a15 15 0 0 0 6.6 6.6l2.2-2.2c.3-.3.7-.4 1-.2 1.1.4 2.3.6 3.6.6.6 0 1 .4 1 1V20c0 .6-.4 1-1 1A17 17 0 0 1 3 4c0-.6.4-1 1-1h3.5c.6 0 1 .4 1 1 0 1.3.2 2.5.6 3.6.1.3 0 .7-.2 1z" fill="#fff"/></svg>
    <div><div class="label">24/7 Phone :</div><div class="value big">+61 (2) 9400 2000</div></div>
  </div>
  <div class="divider" style="left:173px"></div>
  <div class="contact-item" style="left:191px">
    <svg width="16" height="20" viewBox="0 0 16 20"><path d="M8 0a7 7 0 0 0-7 7c0 5 7 13 7 13s7-8 7-13a7 7 0 0 0-7-7zm0 9.6A2.6 2.6 0 1 1 8 4.4a2.6 2.6 0 0 1 0 5.2z" fill="#fff"/></svg>
    <div><div class="label">Address :</div><div class="value">ABN 48 517 903 226<br>Suite G12, 145 Harbour St</div></div>
  </div>
  <div class="divider" style="left:345px"></div>
  <div class="contact-item" style="left:367px">
    <svg width="18" height="14" viewBox="0 0 18 14"><rect x="1" y="1" width="16" height="12" fill="none" stroke="#fff" stroke-width="1.6"/><polyline points="1,1.5 9,8 17,1.5" fill="none" stroke="#fff" stroke-width="1.6"/></svg>
    <div><div class="label">Email :</div><div class="value">info@brooktax.com</div></div>
  </div>
  <div class="divider" style="left:508px"></div>
  <div class="contact-item" style="left:537px">
    <svg width="18" height="18" viewBox="0 0 18 18"><rect x="1" y="5" width="16" height="12" rx="1.5" fill="#fff"/><rect x="5" y="1" width="8" height="5" fill="none" stroke="#fff" stroke-width="1.4"/><g fill="#0b88dc"><rect x="9" y="8" width="2" height="2"/><rect x="12" y="8" width="2" height="2"/><rect x="9" y="11" width="2" height="2"/><rect x="12" y="11" width="2" height="2"/><rect x="3" y="7.5" width="4" height="8"/></g></svg>
    <div><div class="label">Fax :</div><div class="value">61 (2) 9400 2999</div></div>
  </div>
</section>

<h2 class="section-title" style="top:469px">HOW IT WORKS</h2>
<p class="section-lead" style="top:503px">We collect aggregate information on what pages users or visit and information volunteered by the users such as<br>specific requests to be added to our mailing list.</p>

<article class="service-card" style="left:57px">
  <div class="photo" role="img" aria-label="Hand with pen working on financial charts beside a calculator" style="background:linear-gradient(160deg,#e9f0f7 0%,#c9d9ea 50%,#9bb6d1 100%)"></div>
  <span class="num">01.</span><h3>Accounting</h3>
  <p>We collect aggregate information on what pages users or visit and information volunteered by the users such as specific requests to be added to our mailing list.</p>
  <a class="btn">Read More Info</a>
</article>
<article class="service-card" style="left:290px">
  <div class="photo" role="img" aria-label="Businessman drawing a rising growth line" style="background:linear-gradient(150deg,#7d8a99 0%,#3a4350 55%,#1c222b 100%)"></div>
  <span class="num">02.</span><h3>Finance</h3>
  <p>We collect aggregate information on what pages users or visit and information volunteered by the users such as specific requests to be added to our mailing list.</p>
  <a class="btn">Read More Info</a>
</article>
<article class="service-card" style="left:522px">
  <div class="photo" role="img" aria-label="Wooden blocks spelling tax in front of a calculator" style="background:linear-gradient(180deg,#8a8a88 0%,#c49a66 45%,#6b4a33 100%)"></div>
  <span class="num">03.</span><h3>Tax Company</h3>
  <p>We collect aggregate information on what pages users or visit and information volunteered by the users such as specific requests to be added to our mailing list.</p>
  <a class="btn">Read More Info</a>
</article>

<section class="quote">
  <div class="quote-photo" role="img" aria-label="City harbour skyline with a concert hall and a steel arch bridge at sunset"></div>
  <div class="quote-panel">
    <h2>QUOTE REQUEST</h2>
    <p class="lead">We collect aggregate information on what pages users or visit and information<br>such as specific requests to be added to our mailing list.</p>
    <div class="field" style="left:30px;top:94px;width:138px;height:28px">First Name :</div>
    <div class="field" style="left:174px;top:94px;width:138px;height:28px">Last Name :</div>
    <div class="field" style="left:30px;top:127px;width:138px;height:28px">Phone :</div>
    <div class="field" style="left:174px;top:127px;width:138px;height:28px">Email :</div>
    <div class="field" style="left:30px;top:161px;width:282px;height:48px">Message :</div>
    <div class="subscribe">SUBSCRIBE</div>
  </div>
</section>

<footer class="site-footer">
  <p class="copyright">Copyright © 2015 Brook Tax Privacy &amp; Policy .</p>
  <div class="social" style="left:591px" aria-label="Social link"></div>
  <div class="social" style="left:621px" aria-label="Social link"></div>
  <div class="social" style="left:651px" aria-label="Social link"></div>
  <div class="social" style="left:681px" aria-label="Social link"></div>
  <div class="social" style="left:710px" aria-label="Social link"></div>
</footer>

</body>
</html>
```